High end Natural/Therapeutic, skin care company needs packaging design

We need packaging designs for a line of natural cream deodorants made in Canada. They will be launched in retail spas and health stores this fall.
Our company formulates effective, pretty products bought mainly by women ages 35 to 75. These are top shelf products that deliver exceptional value for their cost.
Our company name is "Copper Lantern". We would like Natural Skin Care incorporated as well. The company name should be prominent, legible, duplicatable and recognizable through each product. The product "Deodorant" should be the most prominent. The customer should be able to pick that out easily.
The overall feel of the name and packaging should be feminine, but not frilly. Upscale but not uppity. These are common sense products that make the person feel good about themselves when they see, touch and use them. Each product should have it's own identity, but still have Copper Lantern, Natural Skin Care as the recognizable source.
Our packaging for the deodorants is in clear glass 60 mL jars (55mm height X 55mm diameter, label that goes around it is 1" width X maximum of 6.5" long. Circular label on the top of the lid is 1.67". Information on it is Copper Lantern Natural Skin care and around that is Reveal your true beauty, naturally.) The jar is in a printed box.
The box is 2.5 inches X 2.5 inches X 2.5 inches. No windows in the box.
Solvane Deodorant cream #1, is Sensitive with Lavender as the main essential oil
fragrance. This package should have the feeling of lightness, airiness and femininity. Solvane Deodorant cream #2 is Extra Strength, with Citrus essential oils as the scent. It should have brighter, bolder colors with a slightly masculine feel.
If you leave room for the directions, ingredients and description, I will fill in the body of the information later. Mainly what I am looking for is the font for the name and product and the artistry and color of your designs.
As well as deodorant, Copper Lantern formulates several therapeutic, pain remedies and face serums, toner, and creams. These products use strong, innovative natural ingredients that work for delicate, thin skinned, sensitive skin types. Whenever possible we incorporate Dead Sea minerals from Israel into our products.
Target Market(s)
Women ages 35 to 75
Industry/Entity Type
It Company
Requirements
Must have
- name: COPPER LANTERN Natural Skin Care
Reveal your true beauty, naturally
#1 Solvane Deodorant cream, Sensitive, Lavender
#2 Solvane Deodorant cream Extra Strength, Citrus
Nice to have
- The logo below is what I have been using, but would like to change it. I would like it to look more upscale, bolder, less script. Possibly use Trajan Pro 3 for Copper Lantern and a script for Natural Skin care. As well, I do like the font that the Odette example uses.
I have uploaded some examples of packaging that I like. Hope this helps.
Should not have
- Cartoon, childlike characters. Please do not use the existing Copper Lantern logo, it is for reference only.

```html
<!DOCTYPE html>
<html lang="en">
<head>
<meta charset="utf-8">
<title>Copper Lantern – Solvane Deodorant Cream Labels</title>
<link href="https://fonts.googleapis.com/css2?family=Open+Sans:wght@300;400;600;700&family=Raleway:wght@400&display=swap" rel="stylesheet">
<style>
  :root {
    --bg-top: #c9c8cc;
    --bg-mid: #ececee;
    --bg-bottom: #d6d6d8;
    --label-white: #ffffff;
    --lavender-dark: #4a1645;
    --lavender: #6f1d68;
    --lavender-light: #8d1e80;
    --citrus-dark: #476d22;
    --citrus: #6f9a26;
    --citrus-light: #84ad2a;
    --ink: #2b2b2b;
    --on-colour: #ffffff;
  }
  * { margin: 0; padding: 0; box-sizing: border-box; }
  html, body { width: 1200px; height: 900px; overflow: hidden; }
  body {
    font-family: "Open Sans", Arial, sans-serif;
    background: linear-gradient(180deg, var(--bg-top) 0%, var(--bg-mid) 45%, var(--bg-mid) 70%, var(--bg-bottom) 100%);
    position: relative;
  }
  .wrap-label {
    position: absolute;
    top: 300px;
    width: 340px;
    height: 175px;
    background: var(--label-white);
    box-shadow: 0 2px 8px rgba(0,0,0,0.12);
    overflow: hidden;
  }
  .wrap-label--lavender { left: 238px; --band-a: var(--lavender); --band-b: var(--lavender-dark); --accent: var(--lavender-dark); }
  .wrap-label--citrus { left: 668px; --band-a: var(--citrus-light); --band-b: var(--citrus); --accent: var(--citrus-dark); }
  .wrap-label__band { position: absolute; inset: 0; }
  .brand { position: absolute; left: 62px; top: 34px; color: var(--on-colour); text-align: center; }
  .brand__name { font-size: 16px; letter-spacing: 0.5px; line-height: 1; white-space: nowrap; }
  .brand__name strong { font-weight: 600; }
  .brand__name span { font-weight: 300; }
  .brand__tag { font-size: 10px; font-weight: 400; margin-top: 2px; }
  .sprig {
    position: absolute; left: 98px; top: 98px;
    width: 30px; height: 30px; border-radius: 50%;
    background: rgba(255,255,255,0.85);
  }
  .product {
    position: absolute; right: 12px; top: 76px; text-align: right;
    color: var(--ink); line-height: 1.15;
  }
  .product__line { font-size: 13px; font-weight: 700; color: var(--accent); }
  .product__variant { font-size: 10px; font-weight: 400; }
  .product__scent { font-size: 16px; font-weight: 400; }
  .product__size { font-size: 13px; margin-top: 10px; margin-right: 4px; }
  .product__size small { font-size: 9px; }
  .lid-label { position: absolute; top: 573px; width: 272px; height: 272px; }
  .lid-label--lavender { left: 270px; }
  .lid-label--citrus { left: 714px; }
  .lid-brand { font-family: "Open Sans", Arial, sans-serif; fill: var(--on-colour); }
  .lid-motto { font-family: "Raleway", Arial, sans-serif; fill: var(--on-colour); font-size: 13px; }
</style>
</head>
<body>

<!-- Lavender wrap label -->
<div class="wrap-label wrap-label--lavender">
  <svg class="wrap-label__band" viewBox="0 0 340 175" preserveAspectRatio="none" aria-hidden="true">
    <defs>
      <linearGradient id="band-lavender" x1="0" y1="0" x2="1" y2="0">
        <stop offset="0" stop-color="#6f1d68"/><stop offset="1" stop-color="#4a1645"/>
      </linearGradient>
    </defs>
    <polygon points="0,30 336,3 85,170 0,158" fill="url(#band-lavender)"/>
  </svg>
  <div class="brand">
    <div class="brand__name"><strong>COPPER</strong> <span>LANTERN</span></div>
    <div class="brand__tag">natural skin care</div>
  </div>
  <div class="sprig" role="img" aria-label="Small leaf sprig motif"></div>
  <div class="product">
    <div class="product__line">Solvane</div>
    <div class="product__line">Deodorant cream</div>
    <div class="product__variant">Sensitive</div>
    <div class="product__scent">Lavender</div>
    <div class="product__size">60 <small>ml</small></div>
  </div>
</div>

<!-- Citrus wrap label -->
<div class="wrap-label wrap-label--citrus">
  <svg class="wrap-label__band" viewBox="0 0 340 175" preserveAspectRatio="none" aria-hidden="true">
    <defs>
      <linearGradient id="band-citrus" x1="0" y1="0" x2="1" y2="0">
        <stop offset="0" stop-color="#84ad2a"/><stop offset="1" stop-color="#5f8a22"/>
      </linearGradient>
    </defs>
    <polygon points="0,30 336,3 85,170 0,158" fill="url(#band-citrus)"/>
  </svg>
  <div class="brand">
    <div class="brand__name"><strong>COPPER</strong> <span>LANTERN</span></div>
    <div class="brand__tag">natural skin care</div>
  </div>
  <div class="sprig" role="img" aria-label="Small leaf sprig motif"></div>
  <div class="product">
    <div class="product__line">Solvane</div>
    <div class="product__line">Deodorant cream</div>
    <div class="product__variant">Extra Strength</div>
    <div class="product__scent">Citrus</div>
    <div class="product__size">60 <small>ml</small></div>
  </div>
</div>

<!-- Lavender lid label -->
<svg class="lid-label lid-label--lavender" viewBox="0 0 272 272">
  <defs>
    <radialGradient id="lid-lavender" cx="0.5" cy="0.45" r="0.55">
      <stop offset="0" stop-color="#8d1e80"/><stop offset="1" stop-color="#4a1645"/>
    </radialGradient>
    <path id="motto-arc-lavender" d="M 40 175 A 100 100 0 0 0 236 175"/>
  </defs>
  <circle cx="136" cy="136" r="135" fill="url(#lid-lavender)"/>
  <text class="lid-brand" x="136" y="133" text-anchor="middle" font-size="19"><tspan font-weight="600">COPPER</tspan> <tspan font-weight="300">LANTERN</tspan></text>
  <text class="lid-brand" x="136" y="149" text-anchor="middle" font-size="11">natural skin care</text>
  <text class="lid-motto"><textPath href="#motto-arc-lavender" startOffset="8%">Reveal your true beauty, naturally</textPath></text>
</svg>

<!-- Citrus lid label -->
<svg class="lid-label lid-label--citrus" viewBox="0 0 272 272">
  <defs>
    <radialGradient id="lid-citrus" cx="0.5" cy="0.45" r="0.55">
      <stop offset="0" stop-color="#84ad2a"/><stop offset="1" stop-color="#476d22"/>
    </radialGradient>
    <path id="motto-arc-citrus" d="M 40 175 A 100 100 0 0 0 236 175"/>
  </defs>
  <circle cx="136" cy="136" r="135" fill="url(#lid-citrus)"/>
  <text class="lid-brand" x="136" y="133" text-anchor="middle" font-size="19"><tspan font-weight="600">COPPER</tspan> <tspan font-weight="300">LANTERN</tspan></text>
  <text class="lid-brand" x="136" y="149" text-anchor="middle" font-size="11">natural skin care</text>
  <text class="lid-motto"><textPath href="#motto-arc-citrus" startOffset="8%">Reveal your true beauty, naturally</textPath></text>
</svg>

</body>
</html>
```